Business Card Design

Carl Benson Insurance Agency, an Independent Insurance Agency which was stated on Orchard Lane in Laplace, Louisiana on 1958 and has grown the six locations throughout South Louisiana. We sell personal (auto Homeowners flood, liability) and commercial insurance (commercial property, general liability, workers compensation, commercial auto). I am looking for a double sided card with list the five remaining locations on the back or maybe even a folded four sided card. Our home office is a two story building with a green roof. I have had a logo designed which I have attached. Open for revisions but would like to stay with in the same green roof over an M. I have attached the logo but can not tell if I was uploaded.

Target Market(s)

Individual and commercial insurance buyers. Upper income and business owners

Industry/Entity Type

Insurance

Requirements
Must have
• Must have similar logo as uploaded. Green roof over M or something similar. List all location address and phone numbers.

Employee name, office phone number; direct phone line; email address and website list all locations on card. Very Similar colors to current logo.
Nice to have
• Possible folded card with double sided print

```html
<!DOCTYPE html>
<html lang="en">
<head>
<meta charset="utf-8">
<title>Carl Benson Insurance Agency – Business Card</title>
<link rel="stylesheet" href="https://fonts.googleapis.com/css2?family=Lato:wght@400;700;900&display=swap">
<style>
  :root {
    --bg: #e9e7e2;
    --card: #ffffff;
    --green-dark: #0f4a33;
    --green: #1d6b4b;
    --green-brand: #1f5a3c;
    --blue: #2c6fb3;
    --blue-light: #3f8fd0;
    --grey: #6d6f72;
    --ink: #3b3d3f;
    --white: #ffffff;
  }
  * { box-sizing: border-box; margin: 0; padding: 0; }
  html, body { width: 1200px; height: 1023px; overflow: hidden; }
  body {
    background: var(--bg);
    font-family: "Lato", sans-serif;
    position: relative;
  }
  .card {
    position: absolute;
    width: 640px;
    height: 366px;
    background: var(--card);
    box-shadow: 0 6px 18px rgba(0,0,0,0.18);
    overflow: hidden;
  }
  .card--front { left: 70px; top: 90px; }
  .card--back { left: 490px; top: 567px; }

  /* Front */
  .front__band {
    position: absolute;
    inset: 0;
  }
  .brand {
    position: absolute;
    display: flex;
    align-items: center;
    gap: 14px;
  }
  .brand__square {
    width: 46px; height: 46px;
    background: var(--blue);
    flex: none;
  }
  .brand__name {
    font-weight: 900;
    color: var(--green-brand);
    text-transform: uppercase;
    line-height: 1.05;
    letter-spacing: 0.3px;
    white-space: nowrap;
  }
  .brand__tagline {
    color: var(--grey);
    font-weight: 700;
    white-space: nowrap;
  }
  .card--front .brand { left: 30px; top: 116px; }
  .card--front .brand__square { width: 44px; height: 44px; }
  .card--front .brand__name { font-size: 21px; }
  .card--front .brand__tagline { position: absolute; left: 88px; top: 180px; font-size: 13px; }

  .person { position: absolute; left: 380px; top: 246px; color: var(--white); }
  .person__name { font-size: 22px; font-weight: 700; }
  .person__title { font-size: 15px; margin-top: 3px; }

  .contact {
    position: absolute; left: 380px; top: 54px;
    color: var(--white); font-size: 14px; line-height: 1.55;
    list-style: none;
  }
  .contact__address { margin-bottom: 6px; }
  .contact__item { display: flex; align-items: center; gap: 8px; }
  .contact__item svg { width: 14px; height: 14px; flex: none; }
  .contact__rule {
    position: absolute; left: 380px; top: 226px;
    width: 220px; height: 1px; background: rgba(255,255,255,0.45);
  }

  /* Back */
  .card--back .brand { left: 44px; top: 88px; }
  .card--back .brand__square { width: 60px; height: 60px; }
  .card--back .brand__name { font-size: 34px; }
  .back__tagline { position: absolute; left: 118px; top: 190px; font-size: 24px; color: var(--grey); font-weight: 700; }
  .back__invite { position: absolute; left: 118px; top: 224px; font-size: 17px; color: var(--blue); }
  .locations {
    position: absolute; left: 44px; top: 278px;
    display: flex; gap: 12px; list-style: none;
    font-size: 13px; font-weight: 700; letter-spacing: 1.8px; color: var(--ink);
  }
  .locations li + li::before { content: "•"; margin-right: 12px; color: var(--green-brand); }
</style>
</head>
<body>

<section class="card card--front" aria-label="Business card front">
  <svg class="front__band" viewBox="0 0 640 366" preserveAspectRatio="none" aria-hidden="true">
    <defs>
      <linearGradient id="bandGreen" x1="0" y1="0" x2="1" y2="1">
        <stop offset="0" stop-color="#237552"/>
        <stop offset="1" stop-color="#0f4a33"/>
      </linearGradient>
    </defs>
    <polygon points="352,0 640,0 640,366 322,366" fill="url(#bandGreen)"/>
  </svg>

  <div class="brand">
    <span class="brand__square"></span>
    <span class="brand__name">Carl Benson<br>Insurance Agency</span>
  </div>
  <p class="brand__tagline">Serving Orchard Lane Since 1958</p>

  <ul class="contact">
    <li class="contact__address">2250 Riverbend Pkwy, Suite B<br>Millbrook LA 70412</li>
    <li class="contact__item">
      <svg viewBox="0 0 14 14" aria-hidden="true"><path d="M3 1h3l1 3-2 1a8 8 0 0 0 4 4l1-2 3 1v3c0 1-1 2-2 2A11 11 0 0 1 1 3c0-1 1-2 2-2z" fill="#fff"/></svg>
      555-014-2280
    </li>
    <li class="contact__item">
      <svg viewBox="0 0 14 14" aria-hidden="true"><rect x="3.5" y="1" width="7" height="12" rx="1.2" fill="none" stroke="#fff" stroke-width="1.4"/><circle cx="7" cy="11" r="0.8" fill="#fff"/></svg>
      555-014-2291
    </li>
    <li class="contact__item">
      <svg viewBox="0 0 14 14" aria-hidden="true"><rect x="1" y="3" width="12" height="8" fill="none" stroke="#fff" stroke-width="1.3"/><path d="M1 3l6 5 6-5" fill="none" stroke="#fff" stroke-width="1.3"/></svg>
      tess.hale@carlbenson.com
    </li>
    <li class="contact__item">
      <svg viewBox="0 0 14 14" aria-hidden="true"><rect x="1" y="2" width="12" height="8" fill="none" stroke="#fff" stroke-width="1.3"/><path d="M5 12.5h4M7 10v2.5" stroke="#fff" stroke-width="1.3"/></svg>
      www.carlbensoninsurance.com
    </li>
  </ul>
  <span class="contact__rule"></span>

  <div class="person">
    <p class="person__name">Marla Quinn</p>
    <p class="person__title">Manager</p>
  </div>
</section>

<section class="card card--back" aria-label="Business card back">
  <div class="brand">
    <span class="brand__square"></span>
    <span class="brand__name">Carl Benson<br>Insurance Agency</span>
  </div>
  <p class="back__tagline">Serving Orchard Lane Since 1958</p>
  <p class="back__invite">Visit one of our 6 convenient locations</p>
  <ul class="locations">
    <li>Ashford</li>
    <li>Belmont</li>
    <li>Cedar Vale</li>
    <li>Dunmore</li>
    <li>Elmwood</li>
  </ul>
</section>

</body>
</html>
```